Tablet Presentation to show people how awesome our service is.

Very brief overview of our product, company, and sales person to be shown on a tablet to the customer. We have one now, but it is awful.
Requirement. Needs to give customer a '10' in confidence on our Product, Company, and the Salesperson. I will provide more data as needed.
I will provide info about the sales person, background about the company, such at reviews and history, and information about how the product is better than the competition.

Target Market(s)

It will be shown to the manager of a car dealership in person, on a tablet. It might also be emailed.

Industry/Entity Type

Car Dealer

Font styles to use
Serif
Sans Serif

Requirements
Must have
• It must give the viewer a very high confidence level about 3 aspects of us.
• 1. salesperson showing the presentation, 2. Our product is better than anyone else's', and 3. our company is world class.
• The attached version has a video attached. Has to be easily watched while the sales person is standing, holding the tablet (Velso) in front of the Manager (potential customer)
Nice to have
• It has to be engaging, and keep the viewers interest. It should ask them to do something. Give us a try, or Free demo, etc.
• It needs to focus on their pain points, and let the view know that we are a solution.
Should not have
• Shouldn't be too long.

```html
<!DOCTYPE html>
<html lang="en">
<head>
<meta charset="utf-8">
<title>Arlo Frost – Paint Chip & Scratch Repair Presentation</title>
<link href="https://fonts.googleapis.com/css2?family=Crimson+Text:wght@400;600&family=PT+Sans:wght@400;700&display=swap" rel="stylesheet">
<style>
  :root{
    --red:#9b3a3c;
    --ink:#2b2b2b;
    --grey-head:#5b5b5b;
    --board:#000;
    --backdrop:#b4b4b4;
    --white:#fff;
    --footer-dark:#262626;
    --serif:"Crimson Text", Georgia, serif;
    --sans:"PT Sans", Arial, sans-serif;
  }
  *{box-sizing:border-box;margin:0;padding:0}
  html,body{width:1200px;height:630px;overflow:hidden}
  body{background:var(--backdrop);position:relative;font-family:var(--sans);color:var(--ink)}
  .board{position:absolute;left:0;top:0;width:715px;height:630px;background:var(--board)}
  .slide{position:absolute;width:334px;height:190px;background:var(--white);overflow:hidden}
  .s1{left:16px;top:14px}.s2{left:358px;top:14px}
  .s3{left:16px;top:218px}.s4{left:358px;top:218px}
  .s5{left:16px;top:422px}.s6{left:358px;top:422px}

  .photo{position:absolute;display:block}
  .label-tag{position:absolute;font-family:var(--serif);font-size:10px;padding:0 5px;line-height:13px}
  .label-tag.dark{background:rgba(155,58,60,.75);color:#f0e3e3}
  .label-tag.light{background:var(--white);color:var(--ink)}

  .title-band{position:absolute;left:0;width:100%;background:var(--red);color:var(--white);font-family:var(--serif);text-align:center}

  .brand{position:absolute;display:flex;align-items:center;gap:5px}
  .brand-mark{background:var(--red);flex:none}
  .brand-text{display:flex;flex-direction:column}
  .brand-name{font-family:var(--serif);font-weight:400;color:var(--ink);line-height:1}
  .brand-tag{font-family:var(--sans);color:var(--ink);line-height:1}
  .brand-lg{left:0;width:100%;justify-content:center;top:148px}
  .brand-lg .brand-mark{width:22px;height:22px}
  .brand-lg .brand-name{font-size:17px}
  .brand-lg .brand-tag{font-size:7.5px;margin-top:2px}
  .brand-sm{right:5px;top:7px}
  .brand-sm .brand-mark{width:10px;height:10px}
  .brand-sm .brand-name{font-size:8.5px}
  .brand-sm .brand-tag{font-size:4.2px;margin-top:1px}

  .slide-head{position:absolute;left:0;top:7px;height:14px;border-left:3px solid var(--red);padding-left:4px;font-family:var(--serif);font-weight:400;font-size:14px;line-height:14px;color:var(--red)}

  .slide-foot{position:absolute;left:0;bottom:0;width:100%;height:13px;background:var(--red);display:flex;justify-content:space-between;align-items:center}
  .foot-url{color:var(--white);font-size:6px;padding-left:5px}
  .foot-page{background:var(--footer-dark);color:var(--white);font-size:6px;height:100%;line-height:13px;padding:0 8px}

  .proscons{position:absolute;top:35px;left:14px;right:0;display:grid;grid-template-columns:184px 1fr}
  .proscons ul{list-style:none}
  .proscons li{display:flex;align-items:center;gap:6px;font-size:7px;height:19.5px}
  .tick{width:10px;height:10px;flex:none}

  .area{position:absolute;width:104px}
  .area-name{height:17px;background:var(--grey-head);color:var(--white);font-family:var(--serif);font-size:7.5px;line-height:17px;padding-left:6px;letter-spacing:.2px;white-space:nowrap}
  .area-name.accent{background:var(--red)}
  .area ul{list-style:none;margin-top:5px;padding-left:10px}
  .area li{font-size:7px;height:13.3px;display:flex;align-items:center;gap:6px;white-space:nowrap}
  .area li::before{content:"";width:4px;height:4px;background:var(--red);flex:none}
  .area ul.plain li::before{display:none}

  .thanks{position:absolute;left:0;top:0;width:100%;height:135px;background:linear-gradient(135deg,#a5484a,#8f3335 60%,#a44a4b);color:var(--white);font-family:var(--serif);text-align:center;padding-top:28px}
  .thanks p{font-size:15px;line-height:31px;letter-spacing:.6px}
</style>
</head>
<body>
<main class="board">

  <section class="slide s1">
    <svg class="photo" style="left:0;top:0" width="334" height="112" role="img" aria-label="Close-up of a dark green car fender beside the headlight, chipped on the left and restored on the right">
      <defs><linearGradient id="g1" x1="0" y1="0" x2="1" y2="1"><stop offset="0" stop-color="#2c3a33"/><stop offset=".6" stop-color="#1e2924"/><stop offset="1" stop-color="#39443d"/></linearGradient></defs>
      <rect width="334" height="112" fill="url(#g1)"/>
      <line x1="167" y1="0" x2="167" y2="112" stroke="#e8e8e8" stroke-width="1"/>
      <circle cx="167" cy="62" r="12" fill="none" stroke="#e8e8e8" stroke-width="1.5"/>
    </svg>
    <span class="label-tag dark" style="left:128px;top:5px">Before</span>
    <span class="label-tag dark" style="left:169px;top:5px">After</span>
    <div class="title-band" style="top:112px;height:23px;font-size:14px;line-height:23px">Paint Chip &amp; Scratch Repair</div>
    <div class="brand brand-lg">
      <span class="brand-mark"></span>
      <span class="brand-text"><span class="brand-name">Arlo Frost</span><span class="brand-tag">Expert On-Site Chip Repair</span></span>
    </div>
  </section>

  <section class="slide s2">
    <h2 class="slide-head">The Pro's &amp; Cons</h2>
    <div class="brand brand-sm"><span class="brand-mark"></span><span class="brand-text"><span class="brand-name">Arlo Frost</span><span class="brand-tag">Expert On-Site Chip Repair</span></span></div>
    <div class="proscons">
      <ul>
        <li><svg class="tick" viewBox="0 0 10 10"><path d="M1 5.5 L4 8.5 L9 1.5" fill="none" stroke="var(--red)" stroke-width="1.5"/></svg>Higher profits with in house repairs</li>
        <li><svg class="tick" viewBox="0 0 10 10"><path d="M1 5.5 L4 8.5 L9 1.5" fill="none" stroke="var(--red)" stroke-width="1.5"/></svg>Fixed right on the lot</li>
        <li><svg class="tick" viewBox="0 0 10 10"><path d="M1 5.5 L4 8.5 L9 1.5" fill="none" stroke="var(--red)" stroke-width="1.5"/></svg>No waiting</li>
        <li><svg class="tick" viewBox="0 0 10 10"><path d="M1 5.5 L4 8.5 L9 1.5" fill="none" stroke="var(--red)" stroke-width="1.5"/></svg>We walk the lot for you</li>
        <li><svg class="tick" viewBox="0 0 10 10"><path d="M1 5.5 L4 8.5 L9 1.5" fill="none" stroke="var(--red)" stroke-width="1.5"/></svg>Service you can provide for customers</li>
        <li><svg class="tick" viewBox="0 0 10 10"><path d="M1 5.5 L4 8.5 L9 1.5" fill="none" stroke="var(--red)" stroke-width="1.5"/></svg>Cost efficient</li>
        <li><svg class="tick" viewBox="0 0 10 10"><path d="M1 5.5 L4 8.5 L9 1.5" fill="none" stroke="var(--red)" stroke-width="1.5"/></svg>No Complaints</li>
      </ul>
      <ul>
        <li><svg class="tick" viewBox="0 0 10 10"><path d="M1 5.5 L4 8.5 L9 1.5" fill="none" stroke="var(--red)" stroke-width="1.5"/></svg>Smiles all around</li>
        <li><svg class="tick" viewBox="0 0 10 10"><path d="M1 5.5 L4 8.5 L9 1.5" fill="none" stroke="var(--red)" stroke-width="1.5"/></svg>Small scratches and chips</li>
        <li><svg class="tick" viewBox="0 0 10 10"><path d="M1 5.5 L4 8.5 L9 1.5" fill="none" stroke="var(--red)" stroke-width="1.5"/></svg>Devalued inventory</li>
        <li><svg class="tick" viewBox="0 0 10 10"><path d="M1 5.5 L4 8.5 L9 1.5" fill="none" stroke="var(--red)" stroke-width="1.5"/></svg>Complaints</li>
        <li><svg class="tick" viewBox="0 0 10 10"><path d="M1 5.5 L4 8.5 L9 1.5" fill="none" stroke="var(--red)" stroke-width="1.5"/></svg>Unnecessary body shop work</li>
        <li><svg class="tick" viewBox="0 0 10 10"><path d="M1 5.5 L4 8.5 L9 1.5" fill="none" stroke="var(--red)" stroke-width="1.5"/></svg>Waiting for the car to come back</li>
        <li><svg class="tick" viewBox="0 0 10 10"><path d="M1 5.5 L4 8.5 L9 1.5" fill="none" stroke="var(--red)" stroke-width="1.5"/></svg>Expenses thru the roof</li>
      </ul>
    </div>
    <footer class="slide-foot"><span class="foot-url">www.chipmendauto.com</span><span class="foot-page">Page : 01</span></footer>
  </section>

  <section class="slide s3">
    <h2 class="slide-head">Examples</h2>
    <div class="brand brand-sm"><span class="brand-mark"></span><span class="brand-text"><span class="brand-name">Arlo Frost</span><span class="brand-tag">Expert On-Site Chip Repair</span></span></div>
    <svg class="photo" style="left:0;top:30px" width="334" height="147" role="img" aria-label="Blue car hood and headlight, chipped paint before repair on the left and a clean finish after on the right">
      <defs>
        <linearGradient id="g3a" x1="0" y1="0" x2="1" y2="1"><stop offset="0" stop-color="#2f5f95"/><stop offset=".7" stop-color="#1c3c68"/><stop offset="1" stop-color="#cfd6de"/></linearGradient>
        <linearGradient id="g3b" x1="0" y1="0" x2="1" y2="1"><stop offset="0" stop-color="#3a73b4"/><stop offset=".6" stop-color="#1f4a86"/><stop offset="1" stop-color="#1a2438"/></linearGradient>
      </defs>
      <polygon points="0,0 178,0 140,147 0,147" fill="url(#g3a)"/>
      <polygon points="184,0 334,0 334,147 146,147" fill="url(#g3b)"/>
    </svg>
    <span class="label-tag light" style="left:126px;top:47px">Before</span>
    <span class="label-tag light" style="left:172px;top:73px">After</span>
    <footer class="slide-foot"><span class="foot-url">www.chipmendauto.com</span><span class="foot-page">Page : 01</span></footer>
  </section>

  <section class="slide s4">
    <h2 class="slide-head">Current Dealerships &amp; Groups</h2>
    <div class="area" style="left:0;top:30px"><div class="area-name">HARBOR AUTO MALL</div><ul><li>Crestline Motors</li><li>Parkway Motors</li><li>Parkway Imports</li></ul></div>
    <div class="area" style="left:118px;top:30px"><div class="area-name">BAYSIDE</div><ul><li>Circle Sports Cars</li></ul></div>
    <div class="area" style="left:226px;top:30px"><div class="area-name">WESTFIELD</div><ul><li>Pacific Motors</li><li>Pacific Classics</li><li>SouthBay Autos</li></ul></div>
    <div class="area" style="left:0;top:96px"><div class="area-name">MESA VERDE</div><ul><li>Summit Auto</li><li>Ocean Motors</li><li>Ocean Imports</li></ul></div>
    <div class="area" style="left:118px;top:96px"><div class="area-name">RIDGEVIEW AUTO MALL</div><ul><li>Norwood Trucks</li><li>Norwood Motors</li><li>Ridge Luxury</li></ul></div>
    <div class="area" style="left:226px;top:96px"><div class="area-name accent">GROUPS</div><ul class="plain"><li>Maple Collections</li><li>Crestline Classics</li><li>Coastal Sports Car Club</li></ul></div>
    <footer class="slide-foot"><span class="foot-url">www.chipmendauto.com</span><span class="foot-page">Page : 01</span></footer>
  </section>

  <section class="slide s5">
    <h2 class="slide-head">Examples</h2>
    <div class="brand brand-sm"><span class="brand-mark"></span><span class="brand-text"><span class="brand-name">Arlo Frost</span><span class="brand-tag">Expert On-Site Chip Repair</span></span></div>
    <svg class="photo" style="left:0;top:29px" width="334" height="148" role="img" aria-label="Dark green car fender by the headlight, chipped before repair on the left and restored after on the right">
      <defs>
        <linearGradient id="g5a" x1="0" y1="0" x2="1" y2="1"><stop offset="0" stop-color="#34413a"/><stop offset=".7" stop-color="#26322c"/><stop offset="1" stop-color="#8a8a80"/></linearGradient>
        <linearGradient id="g5b" x1="0" y1="0" x2="1" y2="1"><stop offset="0" stop-color="#2b3832"/><stop offset=".6" stop-color="#1f2a25"/><stop offset="1" stop-color="#6f706a"/></linearGradient>
      </defs>
      <polygon points="0,0 136,0 206,148 0,148" fill="url(#g5a)"/>
      <polygon points="143,0 334,0 334,148 213,148" fill="url(#g5b)"/>
    </svg>
    <span class="label-tag light" style="left:100px;top:47px">Before</span>
    <span class="label-tag light" style="left:200px;top:151px">After</span>
    <footer class="slide-foot"><span class="foot-url">www.chipmendauto.com</span><span class="foot-page">Page : 01</span></footer>
  </section>

  <section class="slide s6">
    <div class="thanks">
      <p>THANK YOU VERY MUCH</p>
      <p>www.chipmendauto.com</p>
      <p>Contact details here</p>
    </div>
    <div class="brand brand-lg">
      <span class="brand-mark"></span>
      <span class="brand-text"><span class="brand-name">Arlo Frost</span><span class="brand-tag">Expert On-Site Chip Repair</span></span>
    </div>
  </section>

</main>
</body>
</html>
```